Letterhead Design Project

I need letterhead designed for my law firm. It would also be used for web based stuff as well.

Industry/Entity Type

Law Firm

```html
<!DOCTYPE html>
<html lang="en">
<head>
<meta charset="utf-8">
<title>Harlow &amp; Venn — Letterhead</title>
<link rel="stylesheet" href="https://fonts.googleapis.com/css2?family=Source+Sans+3:wght@400&display=swap">
<style>
  :root {
    --paper: #ffffff;
    --ink-grey: #5f5f5f;
    --navy: #2a2561;
  }
  html, body {
    margin: 0;
    padding: 0;
    overflow: hidden;
    background: var(--paper);
  }
  .letterhead {
    position: relative;
    width: 844px;
    height: 1200px;
    background: var(--paper);
    font-family: "Source Sans 3", "Myriad Pro", Arial, sans-serif;
    font-size: 16px;
    font-weight: 400;
    color: var(--ink-grey);
    overflow: hidden;
  }
  .sender {
    position: absolute;
    left: 68px;
    top: 31px;
    line-height: 20px;
  }
  .sender p { margin: 0; }
  .sender .address { margin-top: 14px; }

  .firm-name {
    position: absolute;
    left: 356px;
    top: 50px;
    display: flex;
    align-items: center;
    white-space: nowrap;
    line-height: 20px;
  }
  .firm-name__square {
    width: 16px;
    height: 16px;
    margin-right: 10px;
    background: var(--navy);
    flex: none;
  }

  .contact {
    position: absolute;
    left: 566px;
    top: 49px;
    margin: 0;
    padding: 0;
    list-style: none;
  }
  .contact li {
    display: flex;
    align-items: center;
    height: 20px;
  }
  .contact li:nth-child(1) { margin-bottom: 10px; }
  .contact li:nth-child(2) { margin-bottom: 6px; }
  .contact svg { margin-right: 15px; flex: none; }

  .footer-band {
    position: absolute;
    left: 0;
    bottom: 0;
    width: 844px;
    height: 15px;
    background: var(--navy);
  }
</style>
</head>
<body>
<div class="letterhead">
  <div class="sender">
    <p>Name</p>
    <p>Designation</p>
    <p class="address">Address 01, ABC Street</p>
    <p>XYZ lane, London , UK</p>
  </div>

  <div class="firm-name">
    <span class="firm-name__square"></span>
    <span>Harlow &amp; Venn</span>
  </div>

  <ul class="contact">
    <li>
      <svg width="16" height="16" viewBox="0 0 16 16" aria-hidden="true">
        <circle cx="8" cy="8" r="8" fill="var(--navy)"/>
        <text x="8" y="12" text-anchor="middle" font-size="11" fill="#fff" font-family="Source Sans 3, sans-serif">P</text>
      </svg>
      <span>022 XXXXXXXXX</span>
    </li>
    <li>
      <svg width="16" height="16" viewBox="0 0 16 16" aria-hidden="true">
        <circle cx="8" cy="8" r="8" fill="var(--navy)"/>
        <text x="8" y="12" text-anchor="middle" font-size="11" fill="#fff" font-family="Source Sans 3, sans-serif">E</text>
      </svg>
      <span>name@websitename.com</span>
    </li>
    <li>
      <svg width="16" height="16" viewBox="0 0 16 16" aria-hidden="true">
        <circle cx="8" cy="8" r="8" fill="var(--navy)"/>
        <text x="8" y="12" text-anchor="middle" font-size="10" fill="#fff" font-family="Source Sans 3, sans-serif">W</text>
      </svg>
      <span>www.webname.com</span>
    </li>
  </ul>

  <div class="footer-band"></div>
</div>
</body>
</html>
```